Energy drink company looking for a complete can design

Design an energy drink can label using an established trademarked logo along with mandatory nutrition and ingredients table.
We would like to see 3 versions or samples to judge:
1. can design over a black background - called dark color version
2. can design over a white background - called light color version
3. can design over a grey/silver background - called balanced color version

Target Market(s)

USA

Requirements
Must have
• the phrase "yes kelvora energy drink" "yes kelvora" and "ALL Natural Libido Enhancing energy drink" must be on the can somewhere

```html
<!DOCTYPE html>
<html lang="en">
<head>
<meta charset="utf-8">
<title>yes kelvora energy drink — can labels</title>
<link rel="stylesheet" href="https://fonts.googleapis.com/css2?family=Poppins:wght@300;500&display=swap">
<style>
  :root {
    --stage: #d0d0d0;
    --text-light: #ffffff;
    --emblem: #c5283d;
  }
  html, body {
    margin: 0;
    width: 1200px;
    height: 1200px;
    overflow: hidden;
    background: var(--stage);
  }
  .stage {
    position: relative;
    width: 1200px;
    height: 1200px;
  }
  .label {
    position: absolute;
    top: 168px;
    width: 316px;
    height: 863px;
    overflow: hidden;
  }
  .label--dark { left: 68px; --band: #111111; --band-inner: #3a3a3a; }
  .label--light { left: 442px; --band: #ffffff; --band-inner: #d6d6d6; }
  .label--balanced { left: 818px; --band: #c3c3c3; --band-inner: #a9a9a9; }

  .label__art { position: absolute; inset: 0; display: block; }
  .band { fill: var(--band); }
  .band-inner { fill: var(--band-inner); }

  .brand {
    position: absolute;
    left: 28px;
    top: 150px;
    display: flex;
    align-items: center;
    gap: 10px;
  }
  .brand__emblem {
    width: 30px;
    height: 30px;
    border-radius: 50%;
    background: var(--emblem);
    flex: none;
  }
  .brand__name {
    font-family: "Poppins", sans-serif;
    font-weight: 500;
    font-size: 21px;
    line-height: 1;
    letter-spacing: 2px;
    text-transform: uppercase;
    color: var(--text-light);
    white-space: nowrap;
  }
  .version-title {
    position: absolute;
    left: 0;
    right: 0;
    top: 418px;
    text-align: center;
    font-family: "Poppins", sans-serif;
    font-weight: 300;
    font-size: 30px;
    line-height: 36px;
    color: var(--text-light);
  }
  .claim {
    position: absolute;
    left: 0;
    right: 0;
    top: 552px;
    text-align: center;
    font-family: "Poppins", sans-serif;
    font-weight: 300;
    font-size: 17px;
    line-height: 20px;
    letter-spacing: 1px;
    color: var(--text-light);
  }
  .badge {
    position: absolute;
    left: 106px;
    top: 666px;
    width: 108px;
    height: 108px;
  }
  .badge text {
    font-family: "Poppins", sans-serif;
    font-size: 10.5px;
    letter-spacing: 2.4px;
    fill: var(--text-light);
  }
  .volume {
    position: absolute;
    left: 0;
    right: 0;
    top: 828px;
    text-align: center;
    font-family: "Poppins", sans-serif;
    font-weight: 300;
    font-size: 14px;
    color: var(--text-light);
  }
</style>
</head>
<body>
<svg width="0" height="0" style="position:absolute" aria-hidden="true">
  <defs>
    <linearGradient id="gold" x1="0" x2="1" y1="0" y2="0">
      <stop offset="0" stop-color="#ecd089"/>
      <stop offset="0.45" stop-color="#b88a3c"/>
      <stop offset="0.7" stop-color="#8c6126"/>
      <stop offset="1" stop-color="#7b5d3a"/>
    </linearGradient>
    <path id="ring" d="M14 60 a40 40 0 1 1 80 0 a40 40 0 1 1 -80 0"/>
  </defs>
</svg>
<main class="stage">

  <section class="label label--dark" aria-label="Dark color version">
    <svg class="label__art" viewBox="0 0 316 863" aria-hidden="true">
      <rect width="316" height="863" fill="url(#gold)"/>
      <rect y="263" width="316" height="227" fill="#ffffff" opacity="0.08"/>
      <polygon class="band" points="316,19 93,400 316,400"/>
      <polygon class="band-inner" points="316,150 230,290 316,290" opacity="0.6"/>
      <path class="band" d="M316 500 Q285 700 198 863 L316 863 Z"/>
    </svg>
    <div class="brand"><span class="brand__emblem"></span><span class="brand__name">Yes Kelvora</span></div>
    <div class="version-title">Called Dark<br>Color Version</div>
    <div class="claim">ALL NATURAL LIBIDO<br>ENHANCING</div>
    <svg class="badge" viewBox="0 0 108 108" aria-label="Energy drink">
      <text><textPath href="#ring">ENERGY DRINK • ENERGY DRINK •</textPath></text>
      <polygon points="58,32 42,60 53,60 48,82 66,50 55,50 60,32" fill="#ffffff"/>
    </svg>
    <div class="volume">12fl oz (355 ml)</div>
  </section>

  <section class="label label--light" aria-label="Light color version">
    <svg class="label__art" viewBox="0 0 316 863" aria-hidden="true">
      <rect width="316" height="863" fill="url(#gold)"/>
      <rect y="263" width="316" height="227" fill="#ffffff" opacity="0.08"/>
      <polygon class="band" points="316,19 93,400 316,400"/>
      <polygon class="band-inner" points="316,150 230,290 316,290" opacity="0.8"/>
      <path class="band" d="M316 500 Q285 700 198 863 L316 863 Z"/>
    </svg>
    <div class="brand"><span class="brand__emblem"></span><span class="brand__name">Yes Kelvora</span></div>
    <div class="version-title">Called Ligth<br>Color Version</div>
    <div class="claim">ALL NATURAL LIBIDO<br>ENHANCING</div>
    <svg class="badge" viewBox="0 0 108 108" aria-label="Energy drink">
      <text><textPath href="#ring">ENERGY DRINK • ENERGY DRINK •</textPath></text>
      <polygon points="58,32 42,60 53,60 48,82 66,50 55,50 60,32" fill="#ffffff"/>
    </svg>
    <div class="volume">12fl oz (355 ml)</div>
  </section>

  <section class="label label--balanced" aria-label="Balanced color version">
    <svg class="label__art" viewBox="0 0 316 863" aria-hidden="true">
      <rect width="316" height="863" fill="url(#gold)"/>
      <rect y="263" width="316" height="227" fill="#ffffff" opacity="0.08"/>
      <polygon class="band" points="316,19 93,400 316,400"/>
      <polygon class="band-inner" points="316,150 230,290 316,290" opacity="0.8"/>
      <path class="band" d="M316 500 Q285 700 198 863 L316 863 Z"/>
    </svg>
    <div class="brand"><span class="brand__emblem"></span><span class="brand__name">Yes Kelvora</span></div>
    <div class="version-title">Called Balanced<br>Color Version</div>
    <div class="claim">ALL NATURAL LIBIDO<br>ENHANCING</div>
    <svg class="badge" viewBox="0 0 108 108" aria-label="Energy drink">
      <text><textPath href="#ring">ENERGY DRINK • ENERGY DRINK •</textPath></text>
      <polygon points="58,32 42,60 53,60 48,82 66,50 55,50 60,32" fill="#ffffff"/>
    </svg>
    <div class="volume">12fl oz (355 ml)</div>
  </section>

</main>
</body>
</html>
```